Biotech company website design

We are looking for innovative design of our upcoming website. We are a small biotechnology company in Europe dealing with life science products and services.
Updates

Please incorporate the following top level links:
ABOUT US, PRODUCTS, SERVICES, SUPPLIERS, NEWS AND PROMOS, CONTACT US

Target Market(s)

Science people, hospitals, universities ....

Industry/Entity Type

It Company

Requirements
Must have
• Must incorporate our current logo (its color toning)

```html
<!DOCTYPE html>
<html lang="en">
<head>
<meta charset="utf-8">
<title>Meridian BioWorks</title>
<link rel="stylesheet" href="https://fonts.googleapis.com/css2?family=Arimo:ital,wght@0,400;0,700;1,400;1,700&family=PT+Sans:wght@400;700&display=swap">
<style>
  :root{
    --green:#63ad1a;
    --ink:#333333;
    --muted:#555555;
    --line:#e4e4e4;
    --footer:#1c1f26;
    --footer-base:#0d1015;
    --white:#ffffff;
  }
  *{margin:0;padding:0;box-sizing:border-box}
  html,body{width:1138px;height:1200px;overflow:hidden;background:var(--white)}
  body{position:relative;font-family:Arimo,Arial,sans-serif;color:var(--ink)}
  .hero{position:absolute;left:0;top:0;width:1138px;height:491px;
    background:
      radial-gradient(ellipse 140px 220px at 30px 330px,rgba(240,70,110,.75),transparent 70%),
      radial-gradient(ellipse 260px 180px at 620px 330px,rgba(120,190,240,.7),transparent 70%),
      radial-gradient(ellipse 300px 260px at 930px 330px,rgba(255,255,255,.95),transparent 70%),
      radial-gradient(ellipse 180px 120px at 920px 170px,rgba(40,40,45,.55),transparent 70%),
      radial-gradient(ellipse 420px 90px at 420px 140px,rgba(60,120,210,.45),transparent 70%),
      linear-gradient(100deg,#8a5f78 0%,#c58aa6 12%,#dfe6ee 32%,#f3f5f7 50%,#d9e4ee 70%,#eaeef2 100%)}
  .site-header{position:absolute;left:91px;top:0;width:948px;height:94px;background:var(--white)}
  .brand{position:absolute;left:27px;top:31px;display:flex;align-items:center;gap:8px;
    font-family:"PT Sans",sans-serif;font-size:23px;color:var(--ink)}
  .brand-mark{width:26px;height:26px;background:var(--green)}
  .main-nav{position:absolute;right:31px;top:47px;display:flex;gap:15px;font-size:12px;font-weight:700;letter-spacing:.1px}
  .main-nav a{color:var(--ink);text-decoration:none}
  .main-nav a.is-active{color:var(--green)}
  .tagline{position:absolute;left:119px;top:223px;width:298px;height:109px;background:rgba(90,105,80,.55);
    padding:11px 12px 0 14px;font-family:"PT Sans",sans-serif;font-size:19px;line-height:24px;color:var(--white);white-space:nowrap}
  .feature{position:absolute;top:420px;height:215px;background:var(--white);border:1px solid var(--line);padding:8px 7px}
  .feature-photo{height:148px}
  .feature-label{height:46px;background:var(--green);color:var(--white);font-size:12.5px;font-weight:700;padding:15px 14px}
  .divider{position:absolute;left:91px;top:653px;width:948px;height:1px;background:#ececec}
  .welcome-title{position:absolute;left:113px;top:668px;font-size:14px;font-weight:700;color:var(--ink)}
  .welcome-title span{color:var(--green)}
  .welcome-photo{position:absolute;left:110px;top:702px;width:248px;height:134px;
    background:
      radial-gradient(ellipse 90px 70px at 190px 40px,rgba(230,120,130,.5),transparent 70%),
      radial-gradient(ellipse 80px 60px at 40px 110px,rgba(10,10,15,.9),transparent 75%),
      linear-gradient(110deg,#15181d 0%,#3d78ab 40%,#a9cdea 75%,#e4eef7 100%)}
  .welcome-text{position:absolute;left:371px;top:717px;width:345px;font-size:11.3px;line-height:19px;color:var(--muted)}
  .welcome-quote{position:absolute;left:110px;top:855px;width:600px;font-size:13.5px;font-style:italic;font-weight:700;color:var(--green);line-height:16px}
  .news{position:absolute;left:752px;top:668px;width:240px}
  .news h2{font-size:14px;font-weight:700;color:#444;margin-bottom:14px}
  .news-item{border-bottom:1px solid #cfcfcf;padding:0 2px 6px 2px;margin-bottom:9px}
  .news-item:last-child{border-bottom:0}
  .news-date{font-size:11px;font-style:italic;color:var(--green);margin-bottom:8px}
  .news-text{font-size:11.5px;line-height:13.5px;color:var(--muted)}
  .contact{position:absolute;left:0;top:942px;width:1138px;height:195px;background:var(--footer);text-align:center;
    font-family:"PT Sans",sans-serif;color:var(--white)}
  .contact h2{font-weight:400;font-size:16.5px;margin-top:20px}
  .contact p{font-size:13.5px;line-height:16px;margin:24px auto 0;width:540px}
  .social{display:flex;justify-content:center;gap:20px;margin-top:34px}
  .social svg{width:26px;height:26px;fill:none;stroke:var(--white);stroke-width:2.2;stroke-linecap:round;stroke-linejoin:round}
  .legal{position:absolute;left:0;top:1137px;width:1138px;height:63px;background:var(--footer-base);text-align:center;
    font-size:11.5px;line-height:14px;color:#b8bcc4;padding-top:15px}
</style>
</head>
<body>
  <div class="hero" role="img" aria-label="Photo of a scientist in mask and goggles holding a sample tube in a lab with filtration tubing"></div>

  <header class="site-header">
    <div class="brand"><span class="brand-mark"></span>Meridian BioWorks</div>
    <nav class="main-nav">
      <a class="is-active" href="#">ABOUT US</a>
      <a href="#">PRODUCTS</a>
      <a href="#">SERVICES</a>
      <a href="#">SUPPLIERS</a>
      <a href="#">NEWS AND PROMOS</a>
      <a href="#">CONTACT US</a>
    </nav>
  </header>

  <div class="tagline">Meridian strives to provide a high<br>standard of healthcare and<br>improve people’s life</div>

  <div class="feature" style="left:108px;width:288px">
    <div class="feature-photo" role="img" aria-label="Photo of a researcher with safety glasses using a pipette"
      style="background:radial-gradient(ellipse 90px 70px at 170px 80px,rgba(180,130,105,.85),transparent 70%),radial-gradient(ellipse 70px 40px at 180px 25px,rgba(50,40,35,.8),transparent 70%),linear-gradient(120deg,#f0f0f0 0%,#d8d4d0 35%,#a88e7c 60%,#5c6f8e 85%,#e9e9e9 100%)"></div>
    <div class="feature-label">Sed ut persde omnis iste natus</div>
  </div>
  <div class="feature" style="left:412px;width:293px">
    <div class="feature-photo" role="img" aria-label="Photo of a molecule model, flask and microscope"
      style="background:radial-gradient(ellipse 60px 60px at 60px 60px,rgba(20,22,40,.7),transparent 70%),radial-gradient(ellipse 70px 60px at 140px 90px,rgba(230,240,255,.8),transparent 70%),linear-gradient(120deg,#2a3570 0%,#6d84c8 40%,#b7c6ec 70%,#2c3558 100%)"></div>
    <div class="feature-label">Sed ut persde omnis iste natus</div>
  </div>
  <div class="feature" style="left:721px;width:294px">
    <div class="feature-photo" role="img" aria-label="Photo of a gloved hand pipetting into a sample plate"
      style="background:radial-gradient(ellipse 110px 60px at 180px 45px,rgba(245,238,228,.95),transparent 70%),radial-gradient(ellipse 160px 40px at 180px 130px,rgba(60,170,230,.9),transparent 75%),linear-gradient(165deg,#2e2220 0%,#6b5a52 30%,#e6ddd2 55%,#2b86cf 100%)"></div>
    <div class="feature-label">Sed ut persde omnis iste natus</div>
  </div>

  <div class="divider"></div>

  <h1 class="welcome-title">WELCOME TO <span>MERIDIAN BIOWORKS</span></h1>
  <div class="welcome-photo" role="img" aria-label="Photo of a hand holding glass test tubes"></div>
  <p class="welcome-text">Sed ut perspiciatis unde omnis iste natus error sit voluptatem accu doloremque laudantiumtotam rem eaque ipsa quae ab illo inventor is et quasi architecto beatae vitae dicta sunt explicabo. Nemo enim tatem quia voluptas sit aspernatur aut odit aut fugit, sed quia conse magni dolores eos qui ration voluptatem sequi nesciunt.</p>
  <p class="welcome-quote">Sed ut perspiciatis unde omnis iste natus error sit voluptatem accusantiu doloremque laudantium</p>

  <aside class="news">
    <h2>NEWS &amp; PROMOS</h2>
    <div class="news-item"><div class="news-date">Dec 2011</div><div class="news-text">Lorem ipsum dolor sit amet, consectetuer scing elit, sed diam nonummy nibh...</div></div>
    <div class="news-item"><div class="news-date">Oct 2012</div><div class="news-text">Lorem ipsum dolor sit amet, consectetuer scing elit, sed diam nonummy nibh...</div></div>
    <div class="news-item"><div class="news-date">Nov 2013</div><div class="news-text">Lorem ipsum dolor sit amet, consectetuer scing elit, sed diam nonummy nibh...</div></div>
  </aside>

  <footer class="contact">
    <h2>GET IN TOUCH</h2>
    <p>Sed ut perspiciatis unde omnis is natus error sit voluptantium doloremqtium, totam rem aperiam, eaque ipsa quae abtore veritatis et quasi architecto beatae vitae dicta.</p>
    <div class="social" aria-label="Contact links">
      <svg viewBox="0 0 24 24" aria-label="Email"><rect x="3" y="5" width="18" height="14" rx="2"/><path d="M3 7l9 6 9-6"/></svg>
      <svg viewBox="0 0 24 24" aria-label="Phone"><path d="M5 3h4l2 5-2.5 1.5a11 11 0 0 0 6 6L16 13l5 2v4a2 2 0 0 1-2 2A16 16 0 0 1 3 5a2 2 0 0 1 2-2z"/></svg>
      <svg viewBox="0 0 24 24" aria-label="Location"><path d="M12 22s7-7 7-12a7 7 0 0 0-14 0c0 5 7 12 7 12z"/><circle cx="12" cy="10" r="2.5"/></svg>
      <svg viewBox="0 0 24 24" aria-label="Website"><circle cx="12" cy="12" r="9"/><path d="M3 12h18M12 3c3 3 3 15 0 18M12 3c-3 3-3 15 0 18"/></svg>
      <svg viewBox="0 0 24 24" aria-label="Share"><circle cx="6" cy="12" r="2.5"/><circle cx="18" cy="6" r="2.5"/><circle cx="18" cy="18" r="2.5"/><path d="M8.2 10.8l7.6-3.6M8.2 13.2l7.6 3.6"/></svg>
      <svg viewBox="0 0 24 24" aria-label="Next"><path d="M4 12h15M13 6l6 6-6 6"/></svg>
    </div>
  </footer>
  <div class="legal">COPYRIGHT 2013. ALL RIGHTS RESERVED.<br>TERMS &amp; CONDITIONS &nbsp;- &nbsp; PRIVACY &nbsp; - &nbsp; DISCLAIMER</div>
</body>
</html>
```